Meadowlark Behavioral Partners, LLC Needs Modern Business Card Design.

We provide behavioral health services from western Kansas to eastern Kansas. There is an abundance of competition for the services we provide with our main competitor being larger and having significantly more financial resources; however, the quality of services we provide is greater and we have started to catch the attention of the State of Kansas. We had a great logo designed by PixelGuild - this will be used to build upon our brand. The logo (attached) should be used in the card development. We want something unique, modern, but also a card design that clearly states our name, contact info, provides the name and unqiue location of each clinician, etc. Rounded edges, or a unique size, just something that makes our business card stand out from others. I have also uploaded each clinician's name and their unique location and phone number.

Our idea is to have one side be black with our logo. Then, on the other side have business cards for each individual. Plus, we want one card that is "generic" with no specific clinician's name listed so that we can give clients an appointment card when they leave. Some clinicians have two locations - we're open to design and background color, but we have started going with branding colors of black, the yellow in the logo files attached, and sometimes a gray. Our new office has been decorated using this theme.

Target Market(s)

individuals and families in need of behavioral health services; potential professional referral sources; existing referral sources

Industry/Entity Type

Business

Contact Information for Business Card

I attached a Word doc that provides clinician names, credentials and location information specific to each individual.

Font styles to use
Serif

Colors
000000
fbed22
dbdbdb
9d9d9d
c3c3c3

Requirements
Must have
• 1) use of the company logo that has been attached; 2) a template that provides us space to individualize business cards for all of our clinicians; 3) should stick to the colors we are branding with: black, yellow from the logo file, maybe a gray shade and we're open to a suggestion on a shade of white.
Nice to have
• Group discussion culminated in the thought that one side would be black with just our logo - no clinician names, etc. A unique design - rounded edges, unique size, some catchy lay-out would be nice.
Should not have
• Must not be too busy. Should look "clean." The project should stick to branding colors: black, yellow (from the logo file), maybe a gray and shade of white.

```html
<!DOCTYPE html>
<html lang="en">
<head>
<meta charset="utf-8">
<title>Meadowlark Behavioral Partners, LLC — Business Card</title>
<link rel="stylesheet" href="https://fonts.googleapis.com/css2?family=Cinzel:wght@600;700&family=Tinos&display=swap">
<style>
  :root {
    --canvas: #e8e5e0;
    --black: #000000;
    --ink-soft: #1e1e1e;
    --gold: #f5b800;
    --sun-light: #ffd81a;
    --sun-deep: #ffad0f;
    --gray-light: #f2f2f2;
    --gray-mid: #9d9d9d;
    --white: #ffffff;
  }
  * { margin: 0; padding: 0; box-sizing: border-box; }
  html, body { width: 900px; height: 1200px; overflow: hidden; }
  body { background: var(--canvas); position: relative; font-family: "Tinos", "Times New Roman", serif; }

  .card {
    position: absolute;
    left: 107px;
    width: 693px;
    height: 407px;
    overflow: hidden;
    box-shadow: 0 8px 22px rgba(0,0,0,0.35);
  }

  /* Front: logo side */
  .card--front {
    top: 150px;
    border-radius: 0 46px 0 46px;
    background: radial-gradient(ellipse 60% 65% at 50% 40%, #3a3a3a 0%, #151515 55%, var(--black) 100%);
  }
  .brand {
    position: absolute;
    left: 0; right: 0; top: 180px;
    text-align: center;
    font-family: "Cinzel", serif;
    font-weight: 600;
    color: var(--gold);
  }
  .brand__mark {
    display: block;
    width: 46px; height: 46px;
    margin: 0 auto 14px;
    border-radius: 50%;
    background: var(--gold);
  }
  .brand__name { display: block; font-size: 31px; letter-spacing: 1.5px; line-height: 1; }
  .brand__sub { display: block; font-size: 16px; letter-spacing: 1px; margin-top: 8px; line-height: 1; }

  /* Back: clinician side */
  .card--back {
    top: 636px;
    border-radius: 46px 0 46px 0;
    background: linear-gradient(to bottom, var(--gray-light) 0%, #c9c9c9 12%, #6a6a6a 24%, var(--ink-soft) 36%, var(--black) 55%);
  }
  .clinician { position: absolute; left: 51px; top: 52px; font-family: "Cinzel", serif; }
  .clinician__name { font-size: 22px; font-weight: 700; color: var(--black); letter-spacing: 0.5px; line-height: 1; }
  .clinician__title { font-size: 16px; font-weight: 700; color: var(--gold); letter-spacing: 1px; margin-top: 8px; line-height: 1; }

  .contact { position: absolute; left: 51px; top: 287px; color: var(--white); font-size: 15.5px; line-height: 27px; }
  .contact__phone { display: flex; align-items: center; gap: 7px; }
  .contact__icon { width: 19px; height: 19px; }

  .sun-accent { position: absolute; right: 0; bottom: 0; width: 400px; height: 380px; }
</style>
</head>
<body>
  <section class="card card--front" aria-label="Business card front">
    <div class="brand">
      <span class="brand__mark" aria-hidden="true"></span>
      <span class="brand__name">MEADOWLARK</span>
      <span class="brand__sub">BEHAVIORAL PARTNERS, LLC</span>
    </div>
  </section>

  <section class="card card--back" aria-label="Business card back">
    <div class="clinician">
      <p class="clinician__name">DANIEL R. HALE, LP</p>
      <p class="clinician__title">PRESIDENT</p>
    </div>

    <div class="contact">
      <p>418 N. Prairie Ave.</p>
      <p>Hutchinson, Kansas 67501</p>
      <p class="contact__phone">
        <svg class="contact__icon" viewBox="0 0 20 20" aria-hidden="true">
          <rect width="20" height="20" rx="3" fill="var(--gold)"/>
          <path d="M5 6.5c0-1 1-1.8 5-1.8s5 .8 5 1.8v1.2h-2.6V6.6H7.6v1.1H5z M6.5 9h7l1.5 5.5H5z" fill="var(--black)"/>
          <circle cx="10" cy="11.8" r="1.4" fill="var(--gold)"/>
        </svg>
        (620) 555 0182
      </p>
    </div>

    <svg class="sun-accent" viewBox="0 0 400 380" role="img" aria-label="Large brand accent circle">
      <defs>
        <linearGradient id="sunFill" x1="0" y1="0" x2="0" y2="1">
          <stop offset="0" stop-color="var(--sun-light)"/>
          <stop offset="1" stop-color="var(--sun-deep)"/>
        </linearGradient>
      </defs>
      <circle cx="330" cy="360" r="200" fill="url(#sunFill)"/>
    </svg>
  </section>
</body>
</html>
```